Looking for someone to design a business card for my plumbing business Karvel Plumbing Solutions I want the background also to be black, must attract clients. If possible I want the front to be the logo and the back to show maybe the details.

Target Market(s)

Clients

Industry/Entity Type

Plumbing maintenance

Contact Information for Business Card

Name: Dmitri, Contact: 0437 219 608, Email: karvelplumbingsolutions@mailorix.com, Licence number 508217K

Font styles to use
Other font styles liked:
• as per logo maybe?

Colors

Designer to choose colors to be used in the design.

Requirements
Nice to have
• stating the service I provide, emergency plumbing, plumbing maintenance, drainage maintenance, block sewer and stormwater, camera and locating.

```html
<!DOCTYPE html>
<html lang="en">
<head>
<meta charset="utf-8">
<title>Karvel Plumbing Solutions – Business Card</title>
<link href="https://fonts.googleapis.com/css2?family=Montserrat:wght@400;500;800&display=swap" rel="stylesheet">
<style>
  :root {
    --backdrop: #2b2b2d;
    --card-black: #141414;
    --brand-blue: #4f95d6;
    --blue-light: #95c2ea;
    --blue-deep: #1d5a94;
    --white: #ffffff;
  }
  * { box-sizing: border-box; margin: 0; padding: 0; }
  html, body {
    width: 1200px; height: 689px; overflow: hidden;
    background: var(--backdrop);
    font-family: "Montserrat", sans-serif;
  }
  .canvas {
    position: relative; width: 1200px; height: 689px;
    display: flex; align-items: center; justify-content: center; gap: 34px;
  }
  .card {
    position: relative; width: 550px; height: 318px;
    border-radius: 24px; overflow: hidden;
    box-shadow: 0 18px 40px rgba(0,0,0,.45);
  }
  /* Front */
  .card-front {
    background: linear-gradient(100deg, var(--blue-light) 0%, #6aa6dd 35%, var(--brand-blue) 70%);
    display: flex; align-items: center; justify-content: center;
  }
  .brand-front {
    display: flex; align-items: center; gap: 16px;
    color: var(--blue-deep); font-weight: 800; text-transform: uppercase;
  }
  .brand-front .brand-dot {
    width: 46px; height: 46px; border-radius: 50%; background: var(--blue-deep);
  }
  .brand-front .brand-name { line-height: 1; }
  .brand-front .brand-main { font-size: 58px; letter-spacing: 1px; display: block; }
  .brand-front .brand-sub { font-size: 17px; letter-spacing: 1.5px; display: block; margin-top: 6px; }
  /* Back */
  .card-back { background: var(--card-black); }
  .brand-back {
    position: absolute; left: 34px; top: 150px;
    color: var(--white); font-weight: 800; text-transform: uppercase; line-height: 1;
  }
  .brand-back .brand-main { font-size: 46px; display: block; }
  .brand-back .brand-sub { font-size: 13px; letter-spacing: .6px; display: block; margin-top: 6px; }
  .divider {
    position: absolute; left: 252px; top: 62px; width: 2px; height: 160px;
    background: var(--brand-blue);
  }
  .details { position: absolute; left: 272px; top: 64px; color: var(--white); }
  .contact-name {
    color: var(--brand-blue); font-weight: 800; font-size: 30px; letter-spacing: .5px;
  }
  .licence { font-size: 13px; font-weight: 400; margin-top: 12px; }
  .contact-list { list-style: none; margin-top: 28px; }
  .contact-list li {
    display: flex; align-items: center; gap: 8px;
    font-size: 11.2px; font-weight: 400; margin-bottom: 10px; white-space: nowrap;
  }
  .contact-list li.phone { font-size: 13px; }
  .contact-list svg { width: 13px; height: 13px; flex: none; fill: var(--brand-blue); }
</style>
</head>
<body>
<main class="canvas">
  <section class="card card-front" aria-label="Card front">
    <div class="brand-front">
      <span class="brand-dot"></span>
      <span class="brand-name">
        <span class="brand-main">Karvel</span>
        <span class="brand-sub">Plumbing Solutions</span>
      </span>
    </div>
  </section>

  <section class="card card-back" aria-label="Card back">
    <div class="brand-back">
      <span class="brand-main">Karvel</span>
      <span class="brand-sub">Plumbing Solutions</span>
    </div>
    <div class="divider"></div>
    <div class="details">
      <h1 class="contact-name">Dmitri</h1>
      <p class="licence">Licence number 508217K</p>
      <ul class="contact-list">
        <li class="phone">
          <svg viewBox="0 0 24 24" aria-hidden="true"><path d="M6.6 10.8a15.2 15.2 0 0 0 6.6 6.6l2.2-2.2c.3-.3.7-.4 1-.2 1.1.4 2.3.6 3.6.6.6 0 1 .4 1 1V20c0 .6-.4 1-1 1A17 17 0 0 1 3 4c0-.6.4-1 1-1h3.5c.6 0 1 .4 1 1 0 1.3.2 2.5.6 3.6.1.3 0 .7-.2 1z"/></svg>
          0437 219 608
        </li>
        <li class="email">
          <svg viewBox="0 0 24 24" aria-hidden="true"><path d="M2 5h20v14H2zm2 2v.5l8 5 8-5V7zm0 2.8V17h16V9.8l-8 5z"/></svg>
          karvelplumbingsolutions@mailorix.com
        </li>
      </ul>
    </div>
  </section>
</main>
</body>
</html>
```